Design for company homepage promoting to the pharmaceutical industry

Our company produces medical education materials and services for the pharmaceutical industry. Our existing website (www.quorvan.net.au) provides more information.
 
We need a homepage design for our new company website we are creating. Our site will not have a great amount of content, we want it to be fast, user friendly and easily adaptable to viewing on any platform, and through any browser. We don't want it over-designed - i.e. no highly animated banner flags, backgrounds, obscure webfonts, too many graphics etc. Attached are files indicating our existing company logo and design. We want the logo and rings to be retained. We've also attached draft copy for the website.
The final website may be designed in Wordpress (still to be confirmed)
 
This is a design to replace the current site (www.quorvan.net.au). Content will also be revised.
Things we don't like about our current design - doesn't use our current branding, is not very exciting, old fashioned 'standard' format, too much content, just doesn't look that good, boring.
 
Examples of sites we like:
www.brelmot.com.au
http://factsheets.wondipaq.com.au/index.html
 
Features we like from these sites - fast, responsive, short and to the point, cross-platform compatible including smartphones, and looks good
 
Main reasons people will visit our site: to find out whether we can provide services they might be looking for, to make a decision on whether they are interested in what we offer so they can get in touch with us, and to get our contact details.
Main thing we want to achieve from website visits is that it looks good enough and provides enough summary information on us so that they want to get in touch with us, to offer us work or to ask us to come in and meet them to provide more info on what we do.
Two most important calls to action from our website
· make the decision that we can do what you are looking for
· get in touch with us.
Updates

Thanks everyone for your submissions. At this stage with the Christmas break upon us, we are yet to finalise our decision, and will make a decision early in the new year. I hope everyone has a good holiday break.
Kind regards
Doug

Target Market(s)

Pharmaceutical industry professionals, marketers and medical professionals.

Industry/Entity Type

Pharmaceutical

Requirements
Must have
• Company logo and rings must be incorporated, company colour - blue - must be in there.
Should not have
• Complex animation or graphics that will slow the upload or limit cross-platform compatability/viewing on smartphones etc.

```html
<!DOCTYPE html>
<html lang="en">
<head>
<meta charset="utf-8">
<title>Quorvan Healthcare Education</title>
<link rel="stylesheet" href="https://fonts.googleapis.com/css2?family=Open+Sans:wght@400;700&family=Roboto+Slab:wght@400;500&family=Ubuntu:wght@500&display=swap">
<style>
:root{
  --page:#e0e0e0;
  --band:#efefef;
  --white:#ffffff;
  --ink:#222222;
  --body:#666666;
  --muted:#999999;
  --rule:#dddddd;
  --blue:#3a9fd5;
  --tab:#eeeeee;
  --footer:#1e1e1e;
  --footer-text:#585858;
  --footer-head:#ffffff;
  --footer-link:#aaaaaa;
  --footer-rule:#333333;
  --visual-light:#e4e4e4;
  --visual-dark:#cdcdcd;
}
*{box-sizing:border-box;margin:0;padding:0}
html,body{width:964px;height:1200px;overflow:hidden;background:var(--page)}
body{position:relative;font-family:"Open Sans",Arial,sans-serif;color:var(--body)}
h1,h2,h3,h4{font-weight:400}
.abs{position:absolute}
.sheet{left:24px;width:916px;top:0;height:1200px;background:var(--white)}
.prelaunch{left:24px;width:916px;top:32px;height:430px;background:var(--band)}
.prelaunch-title{left:126px;width:336px;top:68px;text-align:center;font-family:"Ubuntu",Arial,sans-serif;font-weight:500;font-size:18px;color:var(--ink)}
.divider{height:12px}
.divider .line{position:absolute;top:6px;height:1px;background:var(--rule)}
.divider svg{position:absolute;top:0}
.lead{left:126px;width:336px;text-align:center;font-size:10.5px;line-height:15.6px;color:var(--body)}
.btn{left:238px;top:314px;width:117px;height:29px;border:1px solid #555;display:flex;align-items:center;justify-content:center;gap:6px;font-size:10px;font-weight:700;color:#333;letter-spacing:.3px}
.product-visual{left:546px;top:126px;width:246px;height:284px;background:linear-gradient(180deg,var(--visual-light) 0%,var(--visual-dark) 100%)}
.section-title{text-align:center;font-family:"Roboto Slab",Rockwell,Georgia,serif;font-weight:400;font-size:15px;color:var(--ink)}
.tabs{left:125px;top:576px;width:343px;height:35px;background:var(--tab);display:flex}
.tab{width:62px;display:flex;align-items:center;justify-content:center;font-size:11px;color:#555}
.tab.active{background:var(--white);border-top:2px solid var(--blue);color:var(--blue);width:65px}
.case-title{left:125px;top:630px;font-family:"Roboto Slab",Rockwell,Georgia,serif;font-weight:400;font-size:16px;color:var(--ink)}
.case-text{left:125px;width:343px;top:664px;text-align:center;font-size:10.5px;line-height:16.8px}
.case-text b{color:#444}
.portrait{left:542px;top:574px;width:74px;height:74px;border-radius:50%;background:radial-gradient(circle at 50% 45%,#d4d4d4,#9a9a9a 72%,#e8e8e8 73%)}
.person-name{left:624px;top:596px;font-family:"Roboto Slab",Rockwell,Georgia,serif;font-weight:400;font-size:16px;color:var(--ink)}
.person-role{left:628px;top:624px;font-size:9px;color:var(--muted)}
.bio{left:528px;width:288px;top:646px;text-align:center;font-size:10.5px;line-height:16.8px}
.clients{left:110px;width:744px;top:935px;height:26px;display:flex;justify-content:space-around;align-items:center}
.client{display:flex;align-items:center;gap:6px;font-family:"Open Sans",Arial,sans-serif;font-weight:700;font-size:14px;color:#555}
.client i{display:block;width:9px;height:9px;border-radius:50%;background:#555}
.arrow{top:940px}
.footer{left:24px;width:916px;top:1034px;height:166px;background:var(--footer)}
.foot-head{top:1074px;font-family:"Roboto Slab",Rockwell,Georgia,serif;font-weight:400;font-size:15px;color:var(--footer-head)}
.foot-about{left:125px;width:210px;top:1108px;font-size:9.5px;line-height:14.4px;color:var(--footer-text)}
.quick{left:372px;width:222px;top:1108px;list-style:none}
.quick li{height:29px;border-bottom:1px solid var(--footer-rule);font-size:11px;color:var(--footer-link);display:flex;align-items:center;gap:8px}
.quick li::before{content:"›";color:#666}
.contact{left:620px;top:1108px;font-size:9.5px;line-height:14px}
.contact dt{position:absolute;left:0;font-weight:700;color:#bbb}
.contact dd{margin-left:50px;color:var(--footer-text);margin-bottom:8px}
</style>
</head>
<body>
<div class="abs sheet"></div>

<section class="abs prelaunch" aria-label="Pre-launch tools"></section>
<h2 class="abs prelaunch-title">Looking for something pre-launch?</h2>
<div class="abs divider" style="left:244px;width:104px;top:116px">
  <span class="line" style="left:0;width:38px"></span>
  <svg style="left:45px" width="14" height="12" viewBox="0 0 14 12"><rect x="1" y="1" width="12" height="7" fill="none" stroke="#aaa"/><line x1="5" y1="10.5" x2="9" y2="10.5" stroke="#aaa"/></svg>
  <span class="line" style="left:66px;width:38px"></span>
</div>
<p class="abs lead" style="top:156px">Quorvan have developed a unique tool for the online management of drug delivery, ideal for implementation in early access and special needs programs.</p>
<p class="abs lead" style="top:226px">And of course Quorvan is an ACCP-accredited provider of continuing professional development activities. We also work closely with other official bodies, including the Apothecary Guild of Australia (AGA) and the National Nursing Collegium (NNC).</p>
<div class="abs btn"><svg width="7" height="9" viewBox="0 0 7 9"><path d="M1.5 1l4 3.5-4 3.5" fill="none" stroke="#333" stroke-width="1.6"/></svg>LEARN MORE</div>
<div class="abs product-visual" role="img" aria-label="Photo of a hand holding a smartphone that shows partner body badges"></div>

<h2 class="abs section-title" style="left:125px;width:343px;top:505px">Some of our Works</h2>
<div class="abs divider" style="left:244px;width:104px;top:545px">
  <span class="line" style="left:0;width:40px"></span>
  <svg style="left:46px" width="12" height="12" viewBox="0 0 12 12"><path d="M6 .5l1.6 3.6 3.9.4-2.9 2.6.8 3.9L6 9 2.6 11l.8-3.9L.5 4.5l3.9-.4z" fill="#ccc"/></svg>
  <span class="line" style="left:64px;width:40px"></span>
</div>
<nav class="abs tabs">
  <span class="tab active">Case 1</span><span class="tab">Case 2</span><span class="tab">Case 3</span>
</nav>
<h3 class="abs case-title">The Cardiovascular Symposium 2008</h3>
<p class="abs case-text"><b>THE CHALLENGE:</b> In 2007, following on from the success of the Cardiqor institute which initially focused more on providing largely business-based content to a broad range of Australian GPs, our client asked us to create a meeting focusing directly on cardiovascular topics. This move was successful, and, based on the largely positive feedback from 2007, the aim for 2008 was to build on this progress and extend the program to include four meetings in four states.</p>

<h2 class="abs section-title" style="left:528px;width:278px;top:505px">Who we are?</h2>
<div class="abs divider" style="left:615px;width:104px;top:545px">
  <span class="line" style="left:0;width:40px"></span>
  <svg style="left:46px" width="12" height="12" viewBox="0 0 12 12"><path d="M6 .5l1.6 3.6 3.9.4-2.9 2.6.8 3.9L6 9 2.6 11l.8-3.9L.5 4.5l3.9-.4z" fill="#ccc"/></svg>
  <span class="line" style="left:64px;width:40px"></span>
</div>
<div class="abs portrait" role="img" aria-label="Portrait photo of the managing director"></div>
<h3 class="abs person-name">Doug Harrowell</h3>
<span class="abs person-role">Managing Director</span>
<p class="abs bio">After graduating with honours from Harlow University, UK, Doug entered the pharmaceutical industry as an information scientist. He soon moved into medical education and entered the competitive European healthcare communications marketplace. He worked for a number of healthcare education agencies in the UK before moving to Australia and setting up Quorvan in 2000.</p>

<div class="abs divider" style="left:125px;width:716px;top:827px">
  <span class="line" style="left:0;width:348px"></span>
  <svg style="left:352px" width="12" height="12" viewBox="0 0 12 12"><path d="M6 .5l1.6 3.6 3.9.4-2.9 2.6.8 3.9L6 9 2.6 11l.8-3.9L.5 4.5l3.9-.4z" fill="#ccc"/></svg>
  <span class="line" style="left:368px;width:348px"></span>
</div>
<h2 class="abs section-title" style="left:125px;width:716px;top:866px;font-size:16px">Our Clients</h2>
<svg class="abs arrow" style="left:86px" width="10" height="16" viewBox="0 0 10 16"><path d="M8 2L2 8l6 6" fill="none" stroke="#ccc" stroke-width="1.6"/></svg>
<div class="abs clients">
  <span class="client"><i></i>Velsano</span>
  <span class="client">Brenhold</span>
  <span class="client">Tamrix</span>
  <span class="client">Ostavia</span>
  <span class="client">Kerrow</span>
</div>
<svg class="abs arrow" style="left:868px" width="10" height="16" viewBox="0 0 10 16"><path d="M2 2l6 6-6 6" fill="none" stroke="#666" stroke-width="1.6"/></svg>

<footer class="abs footer"></footer>
<h4 class="abs foot-head" style="left:125px">About Us</h4>
<div class="abs foot-about">
  <p>All members of our in-house team of project managers, medical writers, designers, administration and production staff are dedicated to delivery on time, on budget, and beyond expectations.</p>
  <p style="margin-top:14px">All members of our in-house team of project</p>
</div>
<h4 class="abs foot-head" style="left:372px">Quick Links</h4>
<ul class="abs quick">
  <li>Who we are?</li>
  <li>What we do?</li>
  <li>Some of our work</li>
</ul>
<h4 class="abs foot-head" style="left:620px">Quorvan Healthcare Education</h4>
<dl class="abs contact">
  <dt>Address:</dt><dd>Level 3, 18 Marden Lane<br>Kellbrook NSW 2199, Australia</dd>
  <dt>Phone:</dt><dd>+61 2 9555 0142</dd>
  <dt>Email:</dt><dd>info@quorvan.net.au</dd>
</dl>
</body>
</html>
```